Security Warning Sign

We have an existing sign that needs an update. I have attached a picture of the current square sign. We need to maintain the same wording. It needs to be professional and appropriate to attach to our customers fence. Also attached is a copy of our building sign which may lend some inspiration and hopefully the ai format will assist. The final sign will be 600mm x 600mmOur website is www.halvorngate.com.au

```html
<!DOCTYPE html>
<html lang="en">
<head>
<meta charset="utf-8">
<title>Halvorngate Security Services – Surveillance Warning Sign</title>
<link rel="stylesheet" href="https://fonts.googleapis.com/css2?family=Archivo+Black&family=Montserrat:wght@700&family=Open+Sans:wght@800&display=swap">
<style>
  :root {
    --hazard-yellow: #ffe500;
    --hazard-black: #0b0b0b;
    --panel-grey: #efefef;
    --ink: #0a0a0a;
    --footer-dark: #2a2a2a;
    --brand-orange: #f5821f;
    --white: #ffffff;
  }
  * { margin: 0; padding: 0; box-sizing: border-box; }
  html, body { width: 1200px; height: 1200px; overflow: hidden; background: var(--panel-grey); }
  .sign { position: relative; width: 1200px; height: 1200px; overflow: hidden; background: var(--panel-grey); }

  .hazard-strip {
    position: absolute; left: 0; width: 1200px;
    background: repeating-linear-gradient(-55deg,
      var(--hazard-yellow) 0 38px, var(--hazard-black) 38px 76px);
  }
  .hazard-strip--top { top: 0; height: 86px; }
  .hazard-strip--bottom { top: 321px; height: 103px; }

  .warning-band {
    position: absolute; top: 86px; left: 0; width: 1200px; height: 235px;
    background: var(--hazard-black);
    display: flex; align-items: center; justify-content: center;
  }
  .warning-title {
    font-family: "Archivo Black", "Arial Black", sans-serif;
    font-size: 178px; line-height: 1; color: var(--white);
    letter-spacing: -2px; white-space: nowrap;
    transform: scaleX(0.93);
  }

  .notice {
    position: absolute; top: 424px; left: 0; width: 1200px; height: 575px;
    display: flex; flex-direction: column; align-items: center; justify-content: center;
    font-family: "Montserrat", Arial, sans-serif; font-weight: 700;
    font-size: 86px; line-height: 98px; color: var(--ink);
    text-align: center; text-transform: uppercase; letter-spacing: 1px;
  }

  .footer { position: absolute; top: 999px; left: 0; width: 1200px; height: 201px; }
  .footer-shapes { position: absolute; inset: 0; }
  .company {
    position: absolute; left: 50px; top: 30px; height: 141px;
    display: flex; align-items: center; gap: 26px;
  }
  .company-dot { width: 120px; height: 120px; border-radius: 50%; background: var(--brand-orange); flex: none; }
  .company-name {
    font-family: "Open Sans", Arial, sans-serif; font-weight: 800;
    font-size: 41px; line-height: 46px; color: var(--white); text-transform: uppercase;
  }
  .contact { position: absolute; left: 670px; top: 0; width: 530px; height: 201px; }
  .contact-icon { position: absolute; left: 18px; top: 28px; width: 84px; height: 110px; }
  .contact-phone {
    position: absolute; left: 110px; top: 38px;
    font-family: "Open Sans", Arial, sans-serif; font-weight: 800;
    font-size: 58px; line-height: 1; color: var(--white); white-space: nowrap;
  }
  .contact-rule { position: absolute; left: 112px; top: 121px; width: 410px; height: 4px; background: var(--hazard-black); }
  .contact-web {
    position: absolute; left: 0; top: 142px; width: 530px; text-align: right; padding-right: 16px;
    font-family: "Open Sans", Arial, sans-serif; font-weight: 800;
    font-size: 24px; line-height: 1; color: var(--white); text-transform: uppercase; white-space: nowrap;
  }
</style>
</head>
<body>
<main class="sign">
  <div class="hazard-strip hazard-strip--top"></div>
  <div class="warning-band"><h1 class="warning-title">!WARNING!</h1></div>
  <div class="hazard-strip hazard-strip--bottom"></div>

  <section class="notice">
    <p>Electronic</p>
    <p>Surveillance</p>
    <p>and Recording</p>
    <p>Devices Installed</p>
    <p>in This Area</p>
  </section>

  <footer class="footer">
    <svg class="footer-shapes" width="1200" height="201" viewBox="0 0 1200 201">
      <rect width="1200" height="201" fill="var(--footer-dark)"/>
      <polygon points="668,0 1200,0 1200,201 612,201" fill="var(--brand-orange)"/>
      <polygon points="690,0 702,0 646,201 634,201" fill="var(--footer-dark)"/>
    </svg>

    <div class="company">
      <span class="company-dot"></span>
      <p class="company-name">Halvorngate<br>Security<br>Services</p>
    </div>

    <div class="contact">
      <svg class="contact-icon" viewBox="0 0 84 110" aria-hidden="true">
        <path d="M62 8 L78 30 L66 42 C58 50 48 64 44 76 L58 86 L46 104 C22 96 10 70 20 42 C28 22 44 12 62 8 Z" fill="var(--footer-dark)"/>
        <path d="M14 30 A34 34 0 0 1 40 10" stroke="var(--footer-dark)" stroke-width="7" fill="none" stroke-linecap="round"/>
        <path d="M4 26 A46 46 0 0 1 36 0" stroke="var(--footer-dark)" stroke-width="6" fill="none" stroke-linecap="round"/>
      </svg>
      <p class="contact-phone">1300 555 014</p>
      <div class="contact-rule"></div>
      <p class="contact-web">www.halvorngate.com.au</p>
    </div>
  </footer>
</main>
</body>
</html>
```